Craft oriented film company needs a Business Card design

Hi all,
We're a 2-man band film company in New Zealand called Kestrel Pictures. We're good honest blokes, who are very passionate about the craft of film making. I've attached our current logo which has a bit of a crafty/artisan feel that we like. Feel free to use it - or throw the baby out with the bathwater and start again..... you never know, you might inspire a complete brand re-work.

In any case, the vibe we want to give out is that we are solid, dependable and no bullshit - but without compromising creative excellence and being in the now. We like the 'Brooklyn' artisan style of work.

Preferably single sided.

We need the standard stuff:
Name, job title, cellphone, email address and physical address (this can be smaller if you like - street, suburb, city & zip, country [if you want])

Check out our website to learn more about us: kestrelpictures.example

Target Market(s)

Brand marketers and advertising agency creatives looking for video production.

Industry/Entity Type

Baby

Requirements
Should not have
• Nothing flashy or too 'futuristic', we want it to feel grounded and real. A limited colour palette is preferred.
We don't want any film reels or cameras or anything obvious like that.

```html
<!DOCTYPE html>
<html lang="en">
<head>
<meta charset="utf-8">
<title>Kestrel Pictures — Business Card</title>
<link rel="stylesheet" href="https://fonts.googleapis.com/css2?family=Roboto:wght@400;700&display=swap">
<style>
  :root {
    --page-bg: #e9e7e3;
    --card-bg: #ffffff;
    --band: #000000;
    --ink-strong: #444444;
    --ink: #4a4a4a;
    --ink-soft: #5a5a5a;
    --rule: #b8b8b8;
    --edge: #8a8a8a;
    --logo-text: #ffffff;
  }
  * { margin: 0; padding: 0; box-sizing: border-box; }
  html, body {
    width: 1200px; height: 755px; overflow: hidden;
    background: var(--page-bg);
    font-family: "Roboto", Arial, sans-serif;
  }
  .card {
    position: absolute; left: 50px; top: 64px;
    width: 1100px; height: 626px;
    background: var(--card-bg);
    border: 2px solid var(--edge);
    overflow: hidden;
  }
  .card__band {
    position: absolute; left: 0; top: 0;
    width: 100%; height: 211px;
    background: var(--band);
  }
  .brand-seal {
    position: absolute; left: 357px; top: 25px;
    width: 288px; height: 288px;
    border-radius: 50%;
    background: var(--band);
    border: 14px solid var(--card-bg);
    display: flex; flex-direction: column;
    align-items: center; justify-content: center;
  }
  .brand-seal__name {
    color: var(--logo-text);
    font-weight: 700; font-size: 38px;
    line-height: 1.1; text-align: center;
    text-transform: uppercase; letter-spacing: 1px;
  }
  .holder {
    position: absolute; right: 612px; top: 400px;
    text-align: right;
  }
  .holder__name {
    font-weight: 700; font-size: 42px;
    color: var(--ink-strong); line-height: 1;
  }
  .holder__title {
    margin-top: 14px;
    font-size: 26px; color: var(--ink-soft);
  }
  .holder__address {
    margin-top: 18px;
    font-size: 27px; line-height: 37px;
    color: var(--ink-soft); font-style: normal;
  }
  .divider {
    position: absolute; left: 518px; top: 405px;
    width: 2px; height: 168px;
    background: linear-gradient(to bottom, rgba(184,184,184,0), var(--rule) 25%, var(--rule) 75%, rgba(184,184,184,0));
  }
  .contacts {
    position: absolute; left: 532px; top: 406px;
    list-style: none;
  }
  .contacts__item {
    display: flex; align-items: center;
    height: 40px; margin-bottom: 20px;
    font-size: 28px; color: var(--ink);
  }
  .contacts__icon {
    width: 24px; height: 24px; margin-right: 14px;
    fill: var(--ink);
  }
</style>
</head>
<body>
  <div class="card">
    <div class="card__band"></div>

    <div class="brand-seal">
      <span class="brand-seal__name">Kestrel<br>Pictures</span>
    </div>

    <div class="holder">
      <p class="holder__name">Your Name</p>
      <p class="holder__title">Title</p>
      <address class="holder__address">street, suburb, city<br>zip, country</address>
    </div>

    <div class="divider"></div>

    <ul class="contacts">
      <li class="contacts__item">
        <svg class="contacts__icon" viewBox="0 0 24 24" aria-hidden="true">
          <path d="M8 1h8a2 2 0 0 1 2 2v18a2 2 0 0 1-2 2H8a2 2 0 0 1-2-2V3a2 2 0 0 1 2-2zm0 3v13h8V4zm4 15a1.2 1.2 0 1 0 0 2.4A1.2 1.2 0 0 0 12 19z"/>
        </svg>
        (123) 456-7890
      </li>
      <li class="contacts__item">
        <svg class="contacts__icon" viewBox="0 0 24 24" aria-hidden="true">
          <path d="M2 6h20v13H2zm2 2v.3l8 5.2 8-5.2V8zm0 2.7V17h16v-6.3l-8 5.2z"/>
        </svg>
        info@kestrelpictures.example
      </li>
      <li class="contacts__item">
        <svg class="contacts__icon" viewBox="0 0 24 24" aria-hidden="true">
          <path d="M12 2a10 10 0 1 0 0 20 10 10 0 0 0 0-20zm0 2c.9 0 2.2 1.8 2.8 5H9.2C9.8 5.8 11.1 4 12 4zM4.3 11h4.6a20 20 0 0 0 0 2H4.3a8 8 0 0 1 0-2zm.8 4h4.1c.3 1.7.8 3.1 1.5 4.2A8 8 0 0 1 5.1 15zm4.1-6H5.1a8 8 0 0 1 5.6-4.2A13 13 0 0 0 9.2 9zm2.8 11c-.9 0-2.2-1.8-2.8-5h5.6c-.6 3.2-1.9 5-2.8 5zm-1-7a18 18 0 0 1 0-2h2a18 18 0 0 1 0 2zm3.3 6.2c.7-1.1 1.2-2.5 1.5-4.2h4.1a8 8 0 0 1-5.6 4.2zM15.1 13a20 20 0 0 0 0-2h4.6a8 8 0 0 1 0 2zm-.3-4a13 13 0 0 0-1.5-4.2A8 8 0 0 1 18.9 9z"/>
        </svg>
        www.kestrelpictures.example
      </li>
    </ul>
  </div>
</body>
</html>
```